A simple and smart interface for busy teachers

We have an existing app (hybrid) on Apple Appstore and Google Playstore that we wish to refresh with some awesome designs and simplified screens.

We would like to stick to our existing colour scheme, see our website morvane.co.nz or screenshots on the appstore for more details and use of colours.

The uploaded files are current screens that we would like redesigned. Specifically, here are additional thoughts on what we wish to see:
1. With the Active Jobs screen, we would prefer to see a week-ly calendar style layout.
2. With Favourites, we would like to see each person's availability going across the page.

Target Market(s)

Middle aged women. (40+). New to tech users.

Industry/Entity Type

Education

Number of Pages Required

5+ page

Font styles to use
Sans Serif

Colors
ec1f27
474747
f78f20

Requirements
Must have
• Calendar view.
• Tidy and sharp info about the jobs.
Nice to have
• Simple and sharp.
Should not have
• Complicated graphics.
• Cluttered designs.
• Too much red. Screens should be mainly white(ish) with red and black.

```html
<!DOCTYPE html>
<html lang="en">
<head>
<meta charset="utf-8">
<title>Profile</title>
<link rel="stylesheet" href="https://fonts.googleapis.com/css2?family=Roboto:wght@300;400&display=swap">
<style>
  :root {
    --brand-red: #d3352a;
    --accent-red: #ec1f27;
    --accent-orange: #f7951f;
    --icon-red: #d8392e;
    --ink: #2a2a2a;
    --body-ink: #333333;
    --rule: #c8c8c8;
    --frame: #d9d9d9;
    --paper: #ffffff;
  }
  * { box-sizing: border-box; margin: 0; padding: 0; }
  html, body {
    width: 675px; height: 1200px; overflow: hidden;
    background: var(--paper);
    font-family: "Roboto", Arial, sans-serif;
  }
  .screen { position: relative; width: 675px; height: 1200px; overflow: hidden; background: var(--paper); }

  .app-bar {
    position: absolute; left: 0; top: 0; width: 675px; height: 95px;
    background: var(--brand-red);
    box-shadow: 0 2px 3px rgba(0,0,0,0.25);
    display: flex; align-items: center; justify-content: center;
  }
  .app-bar__back { position: absolute; left: 26px; top: 31px; width: 24px; height: 32px; }
  .app-bar__title { color: #fff; font-size: 31px; font-weight: 400; letter-spacing: 0.2px; }

  .avatar-frame {
    position: absolute; left: 38px; top: 138px; width: 241px; height: 282px;
    border: 1px solid var(--frame); background: #fff;
  }
  .avatar {
    position: absolute; left: 10px; top: 10px; width: 220px; height: 260px;
    background: linear-gradient(160deg, #5c6560 0%, #4a4f4a 35%, #3a2c26 65%, #7a3b30 100%);
  }

  .identity { position: absolute; left: 318px; top: 140px; width: 330px; }
  .identity__name { color: var(--accent-red); font-size: 32px; font-weight: 400; line-height: 44px; }
  .identity__email { color: var(--ink); font-size: 25px; font-weight: 300; line-height: 36px; }
  .identity__rule { position: absolute; left: 319px; top: 242px; width: 329px; height: 1px; background: var(--rule); }

  .checks { position: absolute; left: 318px; top: 270px; list-style: none; }
  .checks__item {
    display: flex; align-items: center; height: 54px;
    font-size: 25px; font-weight: 300; color: var(--ink);
  }
  .checks__item svg { width: 27px; height: 27px; margin-right: 17px; flex: none; }

  .section-title {
    position: absolute; left: 37px; top: 456px;
    color: var(--accent-red); font-size: 34px; font-weight: 400;
  }
  .description { position: absolute; left: 39px; top: 517px; width: 600px; }
  .description p {
    font-size: 19.5px; font-weight: 300; color: var(--body-ink);
    line-height: 34px; text-align: justify; margin-bottom: 24px;
  }
</style>
</head>
<body>
<div class="screen">
  <header class="app-bar">
    <svg class="app-bar__back" viewBox="0 0 24 32" aria-hidden="true">
      <polyline points="18,4 6,16 18,28" fill="none" stroke="#fff" stroke-width="3.5" stroke-linecap="square"/>
    </svg>
    <h1 class="app-bar__title">Profile</h1>
  </header>

  <div class="avatar-frame">
    <div class="avatar" role="img" aria-label="Portrait photo of the teacher holding a guitar"></div>
  </div>

  <div class="identity">
    <h2 class="identity__name">Rowan Hale</h2>
    <p class="identity__email">rowan@morvane.co.nz</p>
  </div>
  <div class="identity__rule"></div>

  <ul class="checks">
    <li class="checks__item">
      <svg viewBox="0 0 26 26" aria-hidden="true"><circle cx="13" cy="13" r="13" fill="var(--accent-orange)"/><polyline points="7,13.5 11.5,18 19,9.5" fill="none" stroke="#fff" stroke-width="3"/></svg>
      Identity Confirmed
    </li>
    <li class="checks__item">
      <svg viewBox="0 0 26 26" aria-hidden="true"><circle cx="13" cy="13" r="13" fill="var(--accent-orange)"/><polyline points="7,13.5 11.5,18 19,9.5" fill="none" stroke="#fff" stroke-width="3"/></svg>
      Registration Confirmed
    </li>
    <li class="checks__item">
      <svg viewBox="0 0 26 26" aria-hidden="true"><circle cx="13" cy="13" r="13" fill="var(--icon-red)"/><path d="M9 9 L17 17 M17 9 L9 17" stroke="#fff" stroke-width="3" stroke-linecap="round"/></svg>
      Police Vetted
    </li>
  </ul>

  <h3 class="section-title">Description</h3>
  <div class="description">
    <p>I love seeing others develop their love of music more than I love strumming in my guitar with my guidance as a long term relief teacher, the form 4 students of Kestrel Ridge were crowned champions of the 2000 Battle of the Bands.</p>
    <p>Get in touch with me and your students wont be stuck doing theory or scales. They will be exploring the wonder of rhtym and melody.</p>
    <p>Contrary to popular belief, Lorem Ipsum is not simply random text. It has roots in a piece of classical Latin literature from 45 BC, making it over 2000 years old. Tobias Wrenfield, a Latin professor at Ashcombe-Lyle College in Virginia, looked up one of the more obscure Latin words, consectetur, from a Lorem Ipsum passage, and going through the cites of the word in classical literature, discovered the undoubtable source. Lorem Ipsum comes from sections 1.10.32 and 1.10.33 of "de Finibus Bonorum et Malorum" (The Extremes of Good and Evil) by Varenius, written in 45 BC.</p>
  </div>
</div>
</body>
</html>
```